PowerPoint Design Project for Retirement Planning Company

Please design a powerpoint presentation template for our retirement planning company called Pine Harbor Advisors. We need a cover page and slide pages in both portrait and landscape orientation. We make many presentations to clients.

Our tagline is "Retirement Planning. Simplified." We are educators in the retirement planning space. Our company educates small and mid-sized businesses in the board room and break room on how to select a retirement plan for the company and their employees that will help them retire ready. Our slide deck needs to have appeal to a CEO in the board room and a blue collar worker in the breakroom.

We are looking for a template that incorporates our logo, tagline images, colors - green, gray and brown (see uploaded files for examples). The design needs to be clean with plenty of space for text. It needs to be crisp, modern, and eye catching.

We look forward to seeing how you use the images in our business card and logo to achieve a pleasing design. You are the experts so we hope you will develop some innovative designs that wow us and give our clients the confidence that we are experts and put together.
Updates

Designers - Thanks for your great work so far.  

Please do not include the website address on the powerpoint template.

Please provide one template per submission.  When they are grouped together, it is too hard to see the details on your slides.  

Thanks!

Target Market(s)

CEOs and Executive teams at small to medium sized businesses that care about their employees future retirement

Industry/Entity Type

Landscape

Requirements
Must have
• 1) Cover Page (should double as a report cover as well)

2) Second Page for text

3) Third Page for illustrations/graphs/charts

Landscape orientation and Portrait orientation

Colors:

Brown light : C=35, M=60, Y=80, K=25
Brown dark : C=40, M=70, Y=100, K=50

Gray Icon Border: C=0, M=0, Y=0, K=80
Gray Icon Background: C=0, M=0, Y=0, K=5
Gray Letters: C=0, M=0, Y=0, K=80
Gray Light Person: C=0, M=0, Y=0, K=40
Gray Dark Person: C=0, M=0, Y=0, K=60
Gray Dark Wheel Checked: C=0, M=0, Y=0, K=90

Green Light 1: C=40, M=8, Y=85, K=0
Green Light 2: C=53, M=17, Y=100, K=0
Green Dark: C=67, M=39, Y=100, K=27

White: C=0, M=0, Y=0, K=0

Black: C=0, M=0, Y=0, K=100

Fonts:
Logo and graphics files
Footlight MT Light
BrowalliaUPC

Business card/Letterhead files
Calisto MT
Segoe UI

Nice to have
• Please look at the back of our business card design. It has a version of our logo in an abstract form. Consider this concept in full color or a grayed out version as a backdrop.

Use of the "hill" with our tagline is another concept that could be incorporated into the design. See front of our business card and letterhead.

I have uploaded a diagram (wheel diagram full color) that we use to describe our services, plus all the images we use to describe our services (pdf). These images needs to look good as content on a slide.

```html
<!DOCTYPE html>
<html lang="en">
<head>
<meta charset="utf-8">
<title>Pine Harbor Advisors – Presentation Template</title>
<link rel="stylesheet" href="https://fonts.googleapis.com/css2?family=Cinzel:wght@400&family=Source+Sans+3:wght@400;600&display=swap">
<style>
  :root {
    --canvas: #dcdcdc;
    --paper: #ffffff;
    --green-deep: #24300b;
    --green-mid: #3d5514;
    --green-bright: #4f6d1c;
    --pie-green: #64921a;
    --pie-green-side: #4b7113;
    --pie-olive: #7fa41f;
    --pie-lime: #b3d64c;
    --pie-gray: #7b7b7b;
    --pie-charcoal: #545454;
    --pie-charcoal-side: #3d3d3d;
    --swoosh: #8a8a8a;
    --text-gray: #555555;
    --fine-gray: #8c8c8c;
    --rule: #bdbdbd;
    --accent-gold: #f2a900;
    --brand-green: #3d5514;
  }
  * { box-sizing: border-box; margin: 0; padding: 0; }
  html, body { width: 1200px; height: 900px; overflow: hidden; background: var(--canvas); }
  body { position: relative; font-family: "Source Sans 3", "Segoe UI", sans-serif; }

  .slide {
    position: absolute; width: 475px; height: 368px;
    background: var(--paper); overflow: hidden;
  }
  .slide--cover { left: 128px; top: 81px; }
  .slide--text { left: 620px; top: 81px; }
  .slide--chart { left: 128px; top: 463px; }

  .slide__art { position: absolute; inset: 0; width: 100%; height: 100%; }

  .cover__title {
    position: absolute; right: 36px; top: 154px;
    color: #fff; font-weight: 600; font-size: 17px; text-align: right; line-height: 1.1;
  }
  .cover__meta {
    display: block; color: var(--accent-gold); font-weight: 400; font-size: 12px; margin-top: 2px;
  }
  .brand {
    position: absolute; left: 300px; top: 303px;
    display: flex; align-items: center; gap: 6px;
    color: var(--brand-green); font-size: 14px; font-weight: 400; white-space: nowrap;
  }
  .brand__dot { width: 20px; height: 20px; border-radius: 50%; background: var(--brand-green); }

  .slide__heading {
    position: absolute; left: 26px; top: 24px;
    font-family: "Cinzel", "Trajan Pro", serif; font-size: 15px; letter-spacing: 1px;
    color: #fff; font-weight: 400;
  }

  .bullets {
    position: absolute; left: 78px; top: 100px; width: 333px; list-style: none;
    color: var(--text-gray); font-size: 8.6px; line-height: 17.2px; text-align: justify;
  }
  .bullets li { position: relative; text-indent: 0; margin-bottom: 9.5px; }
  .bullets li::before {
    content: ""; position: absolute; left: -10px; top: 5px;
    width: 7px; height: 7px; border-radius: 50%;
    background: radial-gradient(circle at 35% 35%, var(--pie-green) 0 45%, var(--green-deep) 50%);
  }
  .bullets p { text-indent: 0; }

  .body-copy {
    position: absolute; left: 43px; top: 97px; width: 220px;
    color: var(--text-gray); font-size: 8.6px; line-height: 16.8px; text-align: justify;
    hyphens: auto;
  }
  .body-copy p + p { margin-top: 16.8px; }

  .footer {
    position: absolute; left: 21px; right: 22px; top: 346px;
    border-top: 1px solid var(--rule); padding-top: 3px;
    display: flex; justify-content: space-between; align-items: flex-start;
  }
  .footer__note { width: 320px; font-size: 4.4px; line-height: 5px; color: var(--fine-gray); }
  .footer__page { font-size: 6px; color: var(--text-gray); padding-right: 2px; }
</style>
</head>
<body>

<!-- Cover -->
<section class="slide slide--cover" aria-label="Cover slide">
  <svg class="slide__art" viewBox="0 0 495 383" preserveAspectRatio="none" aria-hidden="true">
    <defs>
      <radialGradient id="coverGlow" cx="0.55" cy="0.35" r="0.7">
        <stop offset="0" stop-color="var(--green-bright)"/>
        <stop offset="0.6" stop-color="var(--green-mid)"/>
        <stop offset="1" stop-color="var(--green-deep)"/>
      </radialGradient>
      <linearGradient id="coverSwoosh" x1="0" x2="1">
        <stop offset="0" stop-color="#6e6e6e"/>
        <stop offset="1" stop-color="#c8c8c8" stop-opacity="0"/>
      </linearGradient>
      <linearGradient id="coverBar" x1="0" x2="1">
        <stop offset="0" stop-color="#141a06"/>
        <stop offset="1" stop-color="var(--green-bright)"/>
      </linearGradient>
    </defs>
    <rect width="495" height="383" fill="url(#coverGlow)"/>
    <path d="M0,244 Q140,212 300,224 Q140,226 0,275 Z" fill="url(#coverSwoosh)"/>
    <path d="M0,275 Q240,200 495,250 L495,375 L0,375 Z" fill="#fff"/>
    <rect y="375" width="495" height="8" fill="url(#coverBar)"/>
  </svg>
  <h1 class="cover__title">Lorem ipsum dolor sit amet
    <span class="cover__meta">Birmingham, March 25, 2011</span>
  </h1>
  <div class="brand"><span class="brand__dot"></span>Pine Harbor Advisors</div>
</section>

<!-- Text slide -->
<section class="slide slide--text" aria-label="Text slide">
  <svg class="slide__art" viewBox="0 0 495 383" preserveAspectRatio="none" aria-hidden="true">
    <defs>
      <linearGradient id="headerGreen" x1="0" y1="0" x2="1" y2="0">
        <stop offset="0" stop-color="var(--green-mid)"/>
        <stop offset="0.5" stop-color="var(--green-bright)"/>
        <stop offset="1" stop-color="var(--green-deep)"/>
      </linearGradient>
      <linearGradient id="headerSwoosh" x1="0" x2="1">
        <stop offset="0" stop-color="#6e6e6e"/>
        <stop offset="1" stop-color="#cfcfcf" stop-opacity="0"/>
      </linearGradient>
    </defs>
    <rect width="495" height="110" fill="url(#headerGreen)"/>
    <path d="M0,74 Q120,52 250,55 Q110,62 0,102 Z" fill="url(#headerSwoosh)"/>
    <path d="M0,102 Q240,20 495,80 L495,383 L0,383 Z" fill="#fff"/>
  </svg>
  <h2 class="slide__heading">Presentation Title</h2>
  <ul class="bullets">
    <li>Lorem ipsum dolor sit amet, consectetur adipisicing elit, sed do eiusmod tempor incididunt ut labore et dolore magna aliqua. Ut enim ad minim veniam, quis nostrud exercitation ullamco laboris nisi ut aliquip ex ea commodo consequat. Duis aute irure dolor in reprehenderit in voluptate velit esse cillum dolore eu</li>
    <li>Lorem ipsum dolor sit amet, consectetur adipisicing elit, sed do eiusmod tempor incididunt ut labore et dolore magna aliqua. Ut enim ad minim veniam, quis nostrud exercitation ullamco laboris nisi ut aliquip ex ea commodo consequat. Duis aute irure dolor in reprehenderit in voluptate velit esse cillum dolore eu</li>
    <li>Lorem ipsum dolor sit amet, consectetur adipisicing elit, sed do eiusmod tempor incididunt ut labore et dolore magna aliqua. Ut enim ad minim veniam, quis nostrud exercitation ullamco laboris nisi ut aliquip ex ea commodo consequat. Duis aute irure dolor in reprehenderit in voluptate velit esse cillum dolore eu</li>
  </ul>
  <footer class="footer">
    <p class="footer__note">This material is the property of Pine Harbor Advisors and is shared only with the intended recipient. If you received it in error, please notify the sender and delete it. It is not legal or tax advice.</p>
    <span class="footer__page">2</span>
  </footer>
</section>

<!-- Chart slide -->
<section class="slide slide--chart" aria-label="Chart slide">
  <svg class="slide__art" viewBox="0 0 495 383" preserveAspectRatio="none" aria-hidden="true">
    <defs>
      <linearGradient id="headerGreen2" x1="0" y1="0" x2="1" y2="0">
        <stop offset="0" stop-color="var(--green-mid)"/>
        <stop offset="0.5" stop-color="var(--green-bright)"/>
        <stop offset="1" stop-color="var(--green-deep)"/>
      </linearGradient>
      <linearGradient id="headerSwoosh2" x1="0" x2="1">
        <stop offset="0" stop-color="#6e6e6e"/>
        <stop offset="1" stop-color="#cfcfcf" stop-opacity="0"/>
      </linearGradient>
      <radialGradient id="pieShadow">
        <stop offset="0" stop-color="#9a9a9a"/>
        <stop offset="1" stop-color="#9a9a9a" stop-opacity="0"/>
      </radialGradient>
    </defs>
    <rect width="495" height="110" fill="url(#headerGreen2)"/>
    <path d="M0,74 Q120,52 250,55 Q110,62 0,102 Z" fill="url(#headerSwoosh2)"/>
    <path d="M0,102 Q240,20 495,80 L495,383 L0,383 Z" fill="#fff"/>

    <g class="pie" transform="translate(388 196)">
      <ellipse cx="0" cy="86" rx="90" ry="6" fill="url(#pieShadow)"/>
      <path d="M-86,0 L-86,14 A86 47 0 0 0 86,14 L86,0 A86 47 0 0 1 -86,0 Z" fill="var(--pie-charcoal-side)"/>
      <path d="M29.4,44.2 L29.4,58.2 A86 47 0 0 0 86,14 L86,0 A86 47 0 0 1 29.4,44.2 Z" fill="var(--pie-green-side)"/>
      <path d="M0,0 L0,-47 A86 47 0 0 1 29.4,44.2 Z" fill="var(--pie-green)"/>
      <path d="M0,0 L29.4,44.2 A86 47 0 0 1 -83.1,12.2 Z" fill="var(--pie-charcoal)"/>
      <path d="M0,0 L-83.1,12.2 A86 47 0 0 1 -70.4,-26.9 Z" fill="var(--pie-gray)"/>
      <path d="M0,0 L-70.4,-26.9 A86 47 0 0 1 -36.3,-42.6 Z" fill="var(--pie-lime)"/>
      <path d="M0,0 L-36.3,-42.6 A86 47 0 0 1 0,-47 Z" fill="var(--pie-olive)"/>
    </g>
  </svg>
  <h2 class="slide__heading">Presentation Title</h2>
  <div class="body-copy">
    <p>Lorem ipsum dolor sit amet, consectetur adipisicing elit, sed do eiusmod tempor incididunt ut labore et dolore magna aliqua. Ut enim ad minim veniam, quis nostrud exercitation ullamco laboris nisi ut aliquip ex ea commodo consequat. Duis aute irure dolor in reprehenderit in voluptate velit esse cillum dolore eu fugiat nulla pariatur.</p>
    <p>Lorem ipsum dolor sit amet, consectetur adipisicing elit, sed do eiusmod tempor incididunt ut labore et dolore magna aliqua. Ut enim ad minim veniam, quis nostrud exercitation ullamco laboris nisi ut aliquip ex ea commodo consequat. Duis aute irure dolor in reprehenderit in voluptate velit esse cillum dolore eu fugiat nulla</p>
  </div>
  <footer class="footer">
    <p class="footer__note">This material is the property of Pine Harbor Advisors and is shared only with the intended recipient. If you received it in error, please notify the sender and delete it. It is not legal or tax advice.</p>
    <span class="footer__page">2</span>
  </footer>
</section>

</body>
</html>
```